Consultant needs a simple webpage with WOW effect

I educate advisors in the financial sector in the use of Linkora, Talkzy, ScreenMate etc. for online customer meetings.
My Company has a name (Vaneo) and a domain (vaneo.dk).
VANEO is VArige NEtOpgaver (digital competences in Danish)
I made a terrible mock up via the editor on plixo.com on the domain. Have a look.
I need my logo to be much better (but I would like to keep the 0II0) and the webpage to be totally re-designed and catchy.
The text is in Danish and the headlines is what, how and who (Hvem, hvad og hvordan).
Ideas for a better structure are welcome :-)

Target Group: Human Ressource, technical developers and business developers in financial Companies. In Denmark we do not have a tradition for very "corporate" looks in the finansial sector. I would like creativity and customer value to be on top of mind.

Task: Redesign the logo, design the web page.

```html
<!DOCTYPE html>
<html lang="en">
<head>
<meta charset="utf-8">
<title>Vaneo – Educate Advisors</title>
<link href="https://fonts.googleapis.com/css2?family=Open+Sans:wght@400;600;700;800&family=Oswald:wght@500;600&display=swap" rel="stylesheet">
<style>
  :root {
    --ink: #141414;
    --ink-soft: #1f1f1f;
    --orange: #e8611a;
    --grey-band: #e4e4e4;
    --text: #6a6a6a;
    --partner-text: #4a4a4a;
    --white: #ffffff;
    --footer: #1b1b1b;
    --footer-bottom: #0e0e0e;
  }
  html, body { margin: 0; padding: 0; overflow: hidden; }
  body { font-family: "Open Sans", Arial, sans-serif; background: #fff; }
  .page { position: relative; width: 837px; height: 1200px; overflow: hidden; background: var(--white); }

  /* Header */
  .site-header { height: 78px; background: var(--ink); display: flex; align-items: center; justify-content: space-between; padding: 0 34px 0 28px; box-sizing: border-box; }
  .brand { display: flex; align-items: center; gap: 10px; }
  .brand-dot { width: 14px; height: 14px; border-radius: 50%; background: var(--orange); }
  .brand-text { display: flex; flex-direction: column; }
  .brand-name { font-weight: 800; font-size: 26px; letter-spacing: 1px; color: var(--white); line-height: 1; }
  .brand-tagline { font-size: 8px; color: #9a9a9a; letter-spacing: .5px; margin-top: 3px; }
  .main-nav { display: flex; align-items: center; gap: 4px; }
  .main-nav a { color: var(--white); text-decoration: none; font-size: 10px; font-weight: 600; letter-spacing: .5px; padding: 6px 9px; }
  .main-nav a.active { color: var(--orange); }
  .main-nav .sep { color: #555; font-size: 10px; }
  .search-icon { margin-left: 8px; }

  /* Hero */
  .hero { height: 342px; background: var(--ink); position: relative; }
  .hero-photo { position: absolute; left: 40px; right: 40px; top: 0; bottom: 10px;
    background: linear-gradient(120deg, #8a8f8c 0%, #c9b9a5 35%, #e2d2bd 55%, #9aa2a4 80%, #5d6266 100%); }
  .hero-caption { position: absolute; right: 70px; bottom: 62px; font-family: "Oswald", "Open Sans", sans-serif; font-weight: 600; font-size: 28px; letter-spacing: 1px; color: var(--white); background: rgba(0,0,0,.35); padding: 2px 12px; }

  /* Welcome */
  .welcome { height: 152px; text-align: center; padding-top: 38px; box-sizing: border-box; }
  .welcome h1 { margin: 0 0 12px; font-family: "Oswald", "Open Sans", sans-serif; font-weight: 600; font-size: 22px; color: var(--ink); letter-spacing: .5px; }
  .welcome h1 span { color: var(--orange); }
  .welcome p { margin: 0 auto; width: 740px; font-size: 10px; line-height: 1.6; color: var(--text); }

  /* Cards */
  .pillars { height: 283px; background: var(--grey-band); display: flex; justify-content: center; gap: 32px; padding-top: 18px; box-sizing: border-box; }
  .pillar { width: 210px; height: 246px; background: var(--ink-soft); padding: 10px; box-sizing: border-box; text-align: center; box-shadow: 0 3px 8px rgba(0,0,0,.25); }
  .pillar h2 { margin: 2px 0 10px; font-family: "Oswald", "Open Sans", sans-serif; font-weight: 500; font-size: 15px; color: var(--white); letter-spacing: 1px; }
  .pillar-photo { height: 104px; margin-bottom: 14px; }
  .photo-what { background: linear-gradient(135deg, #4b5560, #8c9aa3 50%, #c7c2b6); }
  .photo-how { background: linear-gradient(135deg, #d8d6d0, #9e8f7c 55%, #5a5148); }
  .photo-who { background: linear-gradient(180deg, #6f8fb3, #2c3e58 70%, #1a2232); }
  .pillar p { margin: 0; font-size: 10px; line-height: 1.6; color: #cfcfcf; }

  /* Call to action band */
  .cta { height: 110px; background: var(--orange); margin-top: 10px; padding: 16px 40px 0; box-sizing: border-box; position: relative; }
  .cta h2 { margin: 0 0 8px; font-family: "Oswald", "Open Sans", sans-serif; font-weight: 500; font-size: 18px; color: var(--white); letter-spacing: .5px; }
  .cta p { margin: 0; width: 560px; font-size: 10px; line-height: 1.6; color: #fde3d2; }
  .cta-button { position: absolute; right: 50px; top: 44px; background: var(--ink); color: var(--white); font-size: 10px; font-weight: 700; letter-spacing: 1px; padding: 11px 28px; text-decoration: none; }

  /* Tools we teach */
  .partners { height: 125px; display: flex; justify-content: center; gap: 30px; align-items: center; }
  .partner { width: 218px; height: 86px; border: 1px solid #d6d6d6; display: flex; align-items: center; justify-content: center; box-sizing: border-box; }
  .partner-name { font-family: "Open Sans", Arial, sans-serif; font-size: 22px; font-weight: 600; color: var(--partner-text); }

  /* Footer */
  .site-footer { position: absolute; left: 0; right: 0; bottom: 0; height: 100px; background: var(--footer); }
  .footer-contact { height: 68px; display: flex; align-items: center; padding: 0 40px; gap: 48px; font-size: 9px; color: #a8a8a8; }
  .contact-item { display: flex; align-items: center; gap: 8px; }
  .social { margin-left: auto; display: flex; gap: 6px; }
  .social span { width: 16px; height: 16px; border-radius: 50%; background: #4a4a4a; }
  .footer-bottom { height: 32px; background: var(--footer-bottom); display: flex; align-items: center; justify-content: space-between; padding: 0 40px; font-size: 8px; color: #7d7d7d; }
  .footer-links span { margin-right: 14px; }
</style>
</head>
<body>
<div class="page">

  <header class="site-header">
    <div class="brand">
      <div class="brand-dot"></div>
      <div class="brand-text">
        <div class="brand-name">VANEO</div>
        <div class="brand-tagline">VArige NEtOpgaver</div>
      </div>
    </div>
    <nav class="main-nav">
      <a class="active" href="#">HOME</a><span class="sep">|</span>
      <a href="#">WHAT</a><span class="sep">|</span>
      <a href="#">HOW</a><span class="sep">|</span>
      <a href="#">WHO</a><span class="sep">|</span>
      <a href="#">CONTACT</a><span class="sep">|</span>
      <svg class="search-icon" width="12" height="12" viewBox="0 0 12 12" aria-hidden="true">
        <circle cx="5" cy="5" r="3.8" fill="none" stroke="#fff" stroke-width="1.5"/>
        <line x1="7.8" y1="7.8" x2="11" y2="11" stroke="#fff" stroke-width="1.6"/>
      </svg>
    </nav>
  </header>

  <section class="hero">
    <div class="hero-photo" role="img" aria-label="Group of young advisors smiling around a laptop"></div>
    <div class="hero-caption">EDUCATE ADVISORS</div>
  </section>

  <section class="welcome">
    <h1>WELCOME TO <span>VANEO</span></h1>
    <p>We train advisors in the financial sector to hold confident online customer meetings. Our courses cover the tools your team already owns, from video calls to shared screens, and turn them into a natural part of daily advice. Short sessions, practical exercises and follow-up support make the change simple, personal and lasting for every advisor.</p>
  </section>

  <section class="pillars">
    <article class="pillar">
      <h2>WHAT</h2>
      <div class="pillar-photo photo-what" role="img" aria-label="Hands working at a desk with laptop and tablets"></div>
      <p>Vaneo trains advisors in the financial sector to run good online customer meetings.</p>
    </article>
    <article class="pillar">
      <h2>HOW</h2>
      <div class="pillar-photo photo-how" role="img" aria-label="Advisor working at a laptop in an office"></div>
      <p>Advisors learn through short, hands-on sessions tailored to their daily tools.</p>
    </article>
    <article class="pillar">
      <h2>WHO</h2>
      <div class="pillar-photo photo-who" role="img" aria-label="Silhouettes of business people against a window"></div>
      <p>For HR, technical and business developers in Danish financial companies.</p>
    </article>
  </section>

  <section class="cta">
    <h2>ONLINE CUSTOMER MEETINGS</h2>
    <p>Book a short talk about how your advisors can meet customers online with ease. We shape each course around your systems, your people and your goals.</p>
    <a class="cta-button" href="#">CLICK HERE</a>
  </section>

  <section class="partners">
    <div class="partner"><span class="partner-name">Linkora</span></div>
    <div class="partner"><span class="partner-name">Talkzy</span></div>
    <div class="partner"><span class="partner-name">ScreenMate</span></div>
  </section>

  <footer class="site-footer">
    <div class="footer-contact">
      <div class="contact-item">
        <svg width="10" height="13" viewBox="0 0 10 13" aria-hidden="true"><path d="M5 0.5a4.3 4.3 0 0 1 4.3 4.3C9.3 8 5 12.5 5 12.5S0.7 8 0.7 4.8A4.3 4.3 0 0 1 5 0.5z" fill="#e8611a"/><circle cx="5" cy="4.8" r="1.5" fill="#1b1b1b"/></svg>
        <span>Nordvej 12, 8000 Aarhus, Denmark</span>
      </div>
      <div class="contact-item">
        <svg width="12" height="12" viewBox="0 0 12 12" aria-hidden="true"><path d="M2.5 0.8l2 2.4-1.2 1.4c.7 1.6 2 2.9 3.6 3.6l1.4-1.2 2.4 2-1 2C5.6 11 1 6.4.5 1.8z" fill="#e8611a"/></svg>
        <span>+45 12 34 56 78</span>
      </div>
      <div class="contact-item">
        <svg width="13" height="10" viewBox="0 0 13 10" aria-hidden="true"><rect x="0.5" y="0.5" width="12" height="9" fill="#e8611a"/><path d="M0.5 0.5l6 5 6-5" fill="none" stroke="#1b1b1b" stroke-width="1"/></svg>
        <span>info@vaneo.dk</span>
      </div>
      <div class="social"><span></span><span></span><span></span><span></span></div>
    </div>
    <div class="footer-bottom">
      <div class="footer-links"><span>Privacy Policy</span><span>Sitemap</span></div>
      <div>© 2015 Vaneo. All rights reserved.</div>
    </div>
  </footer>

</div>
</body>
</html>
```